Brisk Hollow Builders Needs A Flyer

We need a flyer for our newest product "The Cedarlane Garden Workroom"

Here is some copy for the flyer:

1. More and more people everyday are working from home and finding it difficult to disconnect from home activities in order to focus on their work. They are also finding it very expensive to add on to their existing house for a quiet place. Our archatectually stunning, Cedarlane Garden Workroom is the answer. The office studio measures 16' wide and 10' deep. 160 Square feet of space.

Perfect for dozens of purposes. Home office, design studio, artist studio, home school office, reading room, craft studio, drafting room.

Features include:

- Steel Framing. 40-60% lighter then wood, higher strength to weight ratio, resistant to mold and fire and steel is the most recycled material on earth!
- Spray foam insulation. Cool in the summer and warm in the winter.
- HVAC Mini Split with wireless remote control and thermostat.
- 100% Off grid with enough solar and battery storage to run your entire office. No need to pay for an expensive electric installation.
- Flush fitting floor outlets to reduce wires.
- TV mount (Optional with pre-wired electric, HDMI, digital audio & Cat 6)
- Windows are tempered glass custom made by Morvik Glazing.
- Solar qualifies for a 26% tax credit. This is not a write-off rather it is a direct reduction on your tax obligation.
- Thousands of dollars less than adding onto your home.
- Custom color, siding, features available.

This beautiful back yard office is delivered 100% assembled and ready to enjoy on the day of delivery.

We ship nationwide from our factory in South Carolina. Give us a call anytime to speak to a designer and start your dream office today!

555-318-4027
info@BriskHollowBuilders.example

```html
<!DOCTYPE html>
<html lang="en">
<head>
<meta charset="utf-8">
<title>Brisk Hollow Builders – The Cedarlane Garden Workroom</title>
<link rel="stylesheet" href="https://fonts.googleapis.com/css2?family=Lato:wght@300;400;700;900&family=Montserrat:wght@800&display=swap">
<style>
  :root {
    --green: #5aac47;
    --orange: #e9a02e;
    --grey-panel: #ebebea;
    --ink: #1f1f1f;
    --muted: #444;
    --page: #ffffff;
    --backdrop: #d9d6d0;
  }
  * { box-sizing: border-box; margin: 0; padding: 0; }
  html, body { width: 1200px; height: 1200px; overflow: hidden; background: var(--backdrop); }
  .flyer {
    position: absolute; left: 159px; top: 30px;
    width: 928px; height: 1200px;
    transform: scale(0.95); transform-origin: top left;
    background: var(--page);
    font-family: "Lato", sans-serif;
    box-shadow: 0 6px 24px rgba(0,0,0,.18);
    overflow: hidden;
  }
  .abs { position: absolute; }

  .brand { left: 55px; top: 150px; display: flex; align-items: center; gap: 12px; }
  .brand-dot { width: 30px; height: 30px; border-radius: 50%; background: var(--orange); }
  .brand-name { font-weight: 900; font-size: 29px; color: var(--green); letter-spacing: .3px; }

  .banner { left: 0; top: 0; }
  .title {
    left: 455px; top: 133px; width: 460px;
    font-family: "Montserrat", sans-serif; font-weight: 800;
    font-size: 31px; line-height: 43px; color: #fff; text-transform: uppercase;
  }

  .rule { left: 0; width: 928px; background: var(--green); }
  .photos { left: 0; top: 296px; }

  .intro {
    left: 54px; top: 656px; width: 380px;
    font-size: 17.2px; line-height: 20px; color: var(--green); font-weight: 400;
  }
  .intro strong { font-weight: 700; }
  .uses {
    left: 54px; top: 856px; width: 380px;
    font-size: 17.2px; line-height: 20px; color: var(--orange); font-weight: 700;
  }
  .delivery {
    left: 54px; top: 960px; width: 382px; height: 103px;
    background: var(--green); border-radius: 18px;
    display: flex; align-items: center; justify-content: center; text-align: center;
    color: #fff; font-size: 17.2px; line-height: 20px; font-weight: 400;
    padding: 0 30px;
  }
  .shipping { left: 54px; top: 1087px; font-size: 17.2px; color: var(--ink); font-weight: 700; font-weight: 500; }
  .call { left: 54px; top: 1127px; width: 380px; font-size: 17.2px; line-height: 20px; color: var(--ink); }

  .features-title {
    left: 490px; top: 655px; font-size: 18px; color: var(--green); font-weight: 400;
  }
  .features-title::after {
    content: ""; display: block; width: 56px; height: 2px; background: var(--orange); margin-top: 2px;
  }
  .feature { left: 490px; display: flex; gap: 12px; width: 420px; }
  .feature svg { flex: none; width: 24px; height: 24px; margin-top: -2px; }
  .feature p { font-size: 14.2px; line-height: 17px; color: var(--ink); width: 376px; }

  .contact-art { left: 0; top: 0; }
  .contact-line { right: 103px; font-size: 20px; color: #333; font-weight: 400; text-align: right; }
  .contact-icon { left: 840px; width: 34px; height: 34px; }
</style>
</head>
<body>
<article class="flyer">

  <div class="abs brand">
    <span class="brand-name">Brisk Hollow Builders</span>
    <span class="brand-dot"></span>
  </div>

  <svg class="abs banner" width="928" height="240" viewBox="0 0 928 240" aria-hidden="true">
    <polygon points="410,66 928,66 928,120 438,120" fill="var(--orange)"/>
    <polygon points="438,120 928,120 928,230 378,230" fill="var(--green)"/>
  </svg>
  <h1 class="abs title">The Cedarlane Garden<br>Workroom</h1>

  <div class="abs rule" style="top:283px;height:13px"></div>
  <svg class="abs photos" width="928" height="329" viewBox="0 0 928 329" role="img" aria-label="Two renderings of the garden workroom: front view with glass doors, and side view with solar panels on the roof">
    <defs>
      <linearGradient id="photo-left" x1="0" y1="0" x2="0" y2="1">
        <stop offset="0" stop-color="#8fae8a"/>
        <stop offset=".45" stop-color="#4f5a4e"/>
        <stop offset=".75" stop-color="#566f3e"/>
        <stop offset="1" stop-color="#6f8f45"/>
      </linearGradient>
      <linearGradient id="photo-right" x1="0" y1="0" x2="0" y2="1">
        <stop offset="0" stop-color="#b9d3e8"/>
        <stop offset=".3" stop-color="#5c7a45"/>
        <stop offset=".6" stop-color="#45484a"/>
        <stop offset="1" stop-color="#6d9443"/>
      </linearGradient>
    </defs>
    <polygon points="0,0 565,0 365,329 0,329" fill="url(#photo-left)"/>
    <polygon points="580,0 928,0 928,329 380,329" fill="url(#photo-right)"/>
    <polygon points="565,0 580,0 380,329 365,329" fill="var(--green)"/>
  </svg>
  <div class="abs rule" style="top:625px;height:13px"></div>

  <p class="abs intro">More and more people everyday are working from home and finding it difficult to disconnect from home activities in order to focus on their work. They are also finding it very expensive to add on to their existing house for a quiet place. Our archatectually stunning, <strong>Cedarlane Garden Workroom</strong> is the answer. The office studio measures 16' wide and 10' deep. 160 Square feet of space.</p>

  <p class="abs uses">Perfect for dozens of purposes.<br>Home office, design studio, artist studio, home school office, reading room, craft studio, drafting room.</p>

  <p class="abs delivery">This beautiful back yard office is delivered 100% assembled and ready to enjoy on the day of delivery.</p>

  <p class="abs shipping">We ship nationwide from our factory in South Carolina.</p>
  <p class="abs call">Give us a call anytime to speak to a designer<br>and start your dream office today!</p>

  <h2 class="abs features-title">Features include</h2>

  <div class="abs feature" style="top:686px"><svg viewBox="0 0 24 24"><circle cx="12" cy="12" r="12" fill="var(--orange)"/><path d="M6.5 12.5l3.7 3.6 7.3-7.6" fill="none" stroke="#fff" stroke-width="2.6" stroke-linecap="round" stroke-linejoin="round"/></svg><p>Steel Framing. 40-60% lighter then wood, higher strength to weight ratio, resistant to mold and fire and steel is the most recycled material on earth!</p></div>
  <div class="abs feature" style="top:744px"><svg viewBox="0 0 24 24"><circle cx="12" cy="12" r="12" fill="var(--orange)"/><path d="M6.5 12.5l3.7 3.6 7.3-7.6" fill="none" stroke="#fff" stroke-width="2.6" stroke-linecap="round" stroke-linejoin="round"/></svg><p>Spray foam insulation. Cool in the summer and warm in the winter.</p></div>
  <div class="abs feature" style="top:785px"><svg viewBox="0 0 24 24"><circle cx="12" cy="12" r="12" fill="var(--orange)"/><path d="M6.5 12.5l3.7 3.6 7.3-7.6" fill="none" stroke="#fff" stroke-width="2.6" stroke-linecap="round" stroke-linejoin="round"/></svg><p>HVAC Mini Split with wireless remote control and thermostat.</p></div>
  <div class="abs feature" style="top:826px"><svg viewBox="0 0 24 24"><circle cx="12" cy="12" r="12" fill="var(--orange)"/><path d="M6.5 12.5l3.7 3.6 7.3-7.6" fill="none" stroke="#fff" stroke-width="2.6" stroke-linecap="round" stroke-linejoin="round"/></svg><p>100% Off grid with enough solar and battery storage to run your entire office. No need to pay for an expensive electric installation.</p></div>
  <div class="abs feature" style="top:883px"><svg viewBox="0 0 24 24"><circle cx="12" cy="12" r="12" fill="var(--orange)"/><path d="M6.5 12.5l3.7 3.6 7.3-7.6" fill="none" stroke="#fff" stroke-width="2.6" stroke-linecap="round" stroke-linejoin="round"/></svg><p>Flush fitting floor outlets to reduce wires.</p></div>
  <div class="abs feature" style="top:907px"><svg viewBox="0 0 24 24"><circle cx="12" cy="12" r="12" fill="var(--orange)"/><path d="M6.5 12.5l3.7 3.6 7.3-7.6" fill="none" stroke="#fff" stroke-width="2.6" stroke-linecap="round" stroke-linejoin="round"/></svg><p>TV mount (Optional with pre-wired electric, HDMI, digital audio &amp; Cat 6).</p></div>
  <div class="abs feature" style="top:948px"><svg viewBox="0 0 24 24"><circle cx="12" cy="12" r="12" fill="var(--orange)"/><path d="M6.5 12.5l3.7 3.6 7.3-7.6" fill="none" stroke="#fff" stroke-width="2.6" stroke-linecap="round" stroke-linejoin="round"/></svg><p>Windows are tempered glass custom made by Morvik Glazing.</p></div>
  <div class="abs feature" style="top:989px"><svg viewBox="0 0 24 24"><circle cx="12" cy="12" r="12" fill="var(--orange)"/><path d="M6.5 12.5l3.7 3.6 7.3-7.6" fill="none" stroke="#fff" stroke-width="2.6" stroke-linecap="round" stroke-linejoin="round"/></svg><p>Solar qualifies for a 26% tax credit. This is not a write-off rather it is a direct reduction on your tax obligation.</p></div>
  <div class="abs feature" style="top:1030px"><svg viewBox="0 0 24 24"><circle cx="12" cy="12" r="12" fill="var(--orange)"/><path d="M6.5 12.5l3.7 3.6 7.3-7.6" fill="none" stroke="#fff" stroke-width="2.6" stroke-linecap="round" stroke-linejoin="round"/></svg><p>Thousands of dollars less than adding onto your home.</p></div>
  <div class="abs feature" style="top:1061px"><svg viewBox="0 0 24 24"><circle cx="12" cy="12" r="12" fill="var(--orange)"/><path d="M6.5 12.5l3.7 3.6 7.3-7.6" fill="none" stroke="#fff" stroke-width="2.6" stroke-linecap="round" stroke-linejoin="round"/></svg><p>Custom color, siding, features available.</p></div>

  <svg class="abs contact-art" width="928" height="1200" viewBox="0 0 928 1200" aria-hidden="true">
    <path d="M370 1200 Q470 1102 690 1092 L705 1092 Q520 1112 420 1200 Z" fill="var(--orange)"/>
    <path d="M420 1200 Q520 1112 705 1092 L728 1092 Q565 1122 462 1200 Z" fill="var(--green)"/>
    <path d="M462 1200 Q565 1122 728 1092 L928 1092 L928 1200 Z" fill="var(--grey-panel)"/>
  </svg>

  <p class="abs contact-line" style="top:1112px">555-318-4027</p>
  <svg class="abs contact-icon" style="top:1108px" viewBox="0 0 34 34" aria-hidden="true">
    <circle cx="17" cy="17" r="15.5" fill="none" stroke="#111" stroke-width="2"/>
    <path d="M11.5 9.5l3 0 1.5 4-2 1.5a10 10 0 0 0 4 4l1.5-2 4 1.5v3a2 2 0 0 1-2 2A13 13 0 0 1 9.5 11.5a2 2 0 0 1 2-2z" fill="none" stroke="#111" stroke-width="1.7" stroke-linejoin="round"/>
  </svg>
  <p class="abs contact-line" style="top:1153px">info@BriskHollowBuilders.example</p>
  <svg class="abs contact-icon" style="top:1149px" viewBox="0 0 34 34" aria-hidden="true">
    <circle cx="17" cy="17" r="15.5" fill="none" stroke="#111" stroke-width="2"/>
    <rect x="9" y="11.5" width="16" height="11" rx="1" fill="none" stroke="#111" stroke-width="1.7"/>
    <path d="M9.5 12.5l7.5 6 7.5-6" fill="none" stroke="#111" stroke-width="1.7" stroke-linejoin="round"/>
  </svg>

</article>
</body>
</html>
```